Selkirk Boat Lines and Freight Business Card

I need business cards for my new water taxi and freight transport business I have started here in Kodiak Alaska. Kodiak is a remote island in the middle of the gulf of Alaska. There are seven native villages around the island and Kodiak is the #2 fishing port in the United States. We also have the largest Seaward Corps Base in the U.S. My company will be providing water taxi and freight transport logistics to the villages and many hunting and fishing lodges as well as remote properties around the island.

I would like a business card that isn't status quo, something that stands out, either in feel or appearance. I do like clean minimal designs but it needs to have the necessary contact info on it.

Target Market(s)

remote lodge / property owners, residents of the many villages around Kodiak and any one wanting to enjoy the great outdoors of Kodiak Alaska

Industry/Entity Type

Business

Contact Information for Business Card

I like clean simple designs that aren't cluttered but still provide the necessary information

Colors
0255a3
3277b5
33a4d5
9bcb3c
add136
fbed22
ffc214
f78f20
f37122

Requirements
Must have
• logo and contact info
• Captain Marcus Hollend
• www.selkirkboatlines.com
• marcus@selkirkboatlines.com

```html
<!DOCTYPE html>
<html lang="en">
<head>
<meta charset="utf-8">
<title>Selkirk Boat Lines and Freight – Business Card</title>
<link href="https://fonts.googleapis.com/css2?family=Open+Sans:wght@400;600;700&display=swap" rel="stylesheet">
<style>
  :root {
    --backdrop: #8f8f8f;
    --card-white: #ffffff;
    --tab-blue: #29a8e0;
    --brand-blue: #0255a3;
    --accent-blue: #33a4d5;
    --sun-orange: #f78f20;
    --ink: #222222;
    --sky-top: #4a5a72;
    --sky-mid: #8a8f98;
    --sunset: #d9a05a;
    --water: #3a3c40;
    --water-dark: #1c1c1e;
  }
  * { margin: 0; padding: 0; box-sizing: border-box; }
  html, body { width: 1200px; height: 900px; overflow: hidden; }
  body {
    background: var(--backdrop);
    font-family: "Open Sans", Arial, sans-serif;
    position: relative;
  }
  .card {
    position: absolute;
    top: 170px;
    width: 347px;
    height: 561px;
    box-shadow: 0 2px 6px rgba(0,0,0,0.25);
  }
  .card-front { left: 259px; background: var(--card-white); }
  .card-back { left: 631px; overflow: hidden; }

  .tab {
    position: absolute;
    left: 102px;
    width: 143px;
    background: var(--tab-blue);
  }
  .tab-top { top: 0; height: 30px; }
  .tab-bottom { bottom: 0; height: 28px; }

  .brand {
    position: absolute;
    left: 0; right: 0;
    top: 190px;
    text-align: center;
  }
  .brand-mark {
    display: block;
    width: 46px; height: 46px;
    border-radius: 50%;
    background: var(--sun-orange);
    margin: 0 auto 14px;
  }
  .brand-name {
    color: var(--brand-blue);
    font-weight: 700;
    font-size: 27px;
    line-height: 1.2;
  }

  .captain {
    position: absolute;
    left: 0; right: 0;
    top: 352px;
    text-align: center;
    color: var(--accent-blue);
    font-weight: 700;
    font-size: 19px;
  }
  .contact-list {
    position: absolute;
    left: 60px;
    top: 402px;
    list-style: none;
    font-size: 15px;
    color: var(--ink);
  }
  .contact-list li {
    display: flex;
    align-items: center;
    height: 20px;
  }
  .contact-list svg { width: 11px; height: 11px; margin-right: 9px; fill: var(--tab-blue); }

  .scene-photo {
    position: absolute;
    inset: 0;
    background: linear-gradient(180deg,
      var(--sky-top) 0%,
      var(--sky-mid) 32%,
      var(--sunset) 46%,
      var(--water) 56%,
      var(--water-dark) 100%);
  }
  .back-brand {
    position: absolute;
    left: 0; right: 0;
    top: 110px;
    text-align: center;
    color: var(--accent-blue);
    font-weight: 700;
    font-size: 24px;
    line-height: 1.2;
  }
</style>
</head>
<body>
  <section class="card card-front">
    <div class="tab tab-top"></div>
    <div class="brand">
      <span class="brand-mark"></span>
      <div class="brand-name">Selkirk Boat Lines<br>and Freight</div>
    </div>
    <p class="captain">Captain Marcus Hollend</p>
    <ul class="contact-list">
      <li>
        <svg viewBox="0 0 24 24" aria-hidden="true"><path d="M6.6 10.8a15.1 15.1 0 0 0 6.6 6.6l2.2-2.2a1 1 0 0 1 1-.25 11.4 11.4 0 0 0 3.6.57 1 1 0 0 1 1 1V20a1 1 0 0 1-1 1A17 17 0 0 1 3 4a1 1 0 0 1 1-1h3.5a1 1 0 0 1 1 1c0 1.25.2 2.45.57 3.57a1 1 0 0 1-.25 1z"/></svg>
        marcus@selkirkboatlines.com
      </li>
      <li>
        <svg viewBox="0 0 24 24" aria-hidden="true"><path d="M2 5h20v14H2z M2 5l10 7 10-7" /></svg>
        www.selkirkboatlines.com
      </li>
    </ul>
    <div class="tab tab-bottom"></div>
  </section>

  <section class="card card-back">
    <div class="scene-photo" role="img" aria-label="Photo of a boat's wake at sunset, with mountains and calm sea seen from the deck"></div>
    <div class="back-brand">Selkirk Boat Lines<br>and Freight</div>
  </section>
</body>
</html>
```